Property Development Business Cards

I need a business card design for Blue Harbour Developments Pty Ltd. We are a property development company in Australia and our name defines the five values that we adhere to, being Profitable, Partnerships, Quality Developments, Eco Friendly and Enduring Design.

I have attached the current logo that I use, it is just five yellow circles connected to a single cricle in the middle.

Target Market(s)

Our Target audience is real estate agents, owners of properties, builders and other trades

Industry/Entity Type

Business

Requirements
Must have
• Want to have two sides to the card, one with details and one to just highlight the company

```html
<!DOCTYPE html>
<html lang="en">
<head>
<meta charset="utf-8">
<title>Blue Harbour Developments – Business Card</title>
<link href="https://fonts.googleapis.com/css2?family=PT+Sans:wght@400;700&family=PT+Sans+Narrow:wght@400&display=swap" rel="stylesheet">
<style>
  :root {
    --blue-light: #5b9fe0;
    --blue-mid: #3b7fcb;
    --blue-dark: #2a66b0;
    --sun: #f7e43a;
    --sun-deep: #e8c81a;
    --tagline: #f4f0a0;
    --white: #ffffff;
    --ink: #1c1c1c;
    --rule: #e46a78;
    --page: #ffffff;
  }
  * { margin: 0; padding: 0; box-sizing: border-box; }
  html, body {
    width: 900px;
    height: 1200px;
    overflow: hidden;
    background: var(--page);
    font-family: "PT Sans", Arial, sans-serif;
    color: var(--ink);
  }
  .canvas { position: relative; width: 900px; height: 1200px; }

  /* Front side */
  .card-front {
    position: absolute;
    left: 0; top: 0;
    width: 900px; height: 612px;
    background: radial-gradient(circle at 80% 10%, var(--blue-light) 0%, var(--blue-mid) 45%, var(--blue-dark) 100%);
  }
  .front-mark {
    position: absolute;
    left: 70px; top: 70px;
    display: flex; align-items: center; gap: 26px;
  }
  .front-mark .dot {
    width: 130px; height: 130px; border-radius: 50%;
    background: radial-gradient(circle at 40% 35%, var(--sun) 0%, var(--sun-deep) 100%);
  }
  .front-mark .mark-name {
    font-size: 34px; font-weight: 400; color: var(--white);
  }
  .front-name {
    position: absolute;
    left: 44px; top: 408px;
    font-size: 46px; font-weight: 400; color: var(--white);
    letter-spacing: 0.3px;
  }
  .front-tagline {
    position: absolute;
    left: 44px; top: 475px;
    font-family: "PT Sans Narrow", "Arial Narrow", sans-serif;
    font-size: 20px; color: var(--tagline);
    word-spacing: 2px;
  }

  /* Back side */
  .card-back {
    position: absolute;
    left: 0; top: 640px;
    width: 900px; height: 560px;
    background: var(--white);
  }
  .card-back .rule { position: absolute; left: 0; top: 0; }
  .back-mark {
    position: absolute;
    left: 36px; top: 78px;
    display: flex; align-items: center; gap: 16px;
  }
  .back-mark .dot {
    width: 70px; height: 70px; border-radius: 50%;
    background: var(--sun);
  }
  .back-mark .mark-name { font-size: 26px; color: var(--ink); }

  .person {
    position: absolute;
    left: 456px; top: 132px;
  }
  .person-name { font-size: 32px; font-weight: 400; margin-bottom: 26px; }
  .person-line { font-size: 20px; line-height: 34px; }

  .company {
    position: absolute;
    left: 36px; top: 376px;
  }
  .company-name { font-size: 44px; line-height: 52px; }
  .company-name .suffix { font-size: 30px; }
  .company-line { font-size: 28px; line-height: 44px; }
</style>
</head>
<body>
<main class="canvas">
  <section class="card-front">
    <div class="front-mark">
      <span class="dot"></span>
      <span class="mark-name">Blue Harbour</span>
    </div>
    <h1 class="front-name">Blue Harbour Developments</h1>
    <p class="front-tagline">Profitability | Partnerships | Quality | Sustainability | Endurance</p>
  </section>

  <section class="card-back">
    <svg class="rule" width="900" height="560" viewBox="0 0 900 560" aria-hidden="true">
      <polyline points="0,1 885,1 885,560" fill="none" stroke="#e46a78" stroke-width="2"/>
    </svg>
    <div class="back-mark">
      <span class="dot"></span>
      <span class="mark-name">Blue Harbour</span>
    </div>
    <div class="person">
      <p class="person-name">Daniel Marsh</p>
      <p class="person-line">m: 0412 555 019</p>
      <p class="person-line">e: Daniel@BlueHarbourDevelopments.com.au</p>
    </div>
    <div class="company">
      <p class="company-name">Blue Harbour Developments <span class="suffix">Pty Ltd</span></p>
      <p class="company-line">PO Box 118 | Kingston | ACT | 2604 | Australia</p>
      <p class="company-line">www.BlueHarbourDevelopments.com.au</p>
    </div>
  </section>
</main>
</body>
</html>
```